zumoKet - website to pay membership association fee

The main purpose of this site it to allow a pre-registered user to be able to view the membership fees for their membership association and pay the same in one of the ways offered by the portal.
You are required to create a graphical project only for the logon functions as a user, while omitting the back end/administration ones that will be decided later
The site, besides being responsive must be very intuitive in its function. The graphics must be bright.

Number of Pages Required

4 page

Requirements
Must have
• i need to see template for
• 1. Home page
• 2. Page after login. People can se one or more bill to Pay and decide to see more details or to pay.
• 3. Page to Pay. Choose the desired payment method five alternative

```html
<!DOCTYPE html>
<html lang="en">
<head>
<meta charset="utf-8">
<title>zumoKet – Make a Payment</title>
<link rel="stylesheet" href="https://fonts.googleapis.com/css2?family=Fredoka:wght@500;600&family=Lato:wght@400;700;900&display=swap">
<style>
  :root {
    --blue: #1d9ad6;
    --green: #55ab48;
    --stone: #c9c3c3;
    --panel: #ececec;
    --white: #ffffff;
    --ink: #111111;
    --icon: #231f20;
  }
  * { box-sizing: border-box; margin: 0; padding: 0; }
  html, body { width: 1200px; height: 1090px; overflow: hidden; }
  body { background: var(--stone); font-family: "Lato", sans-serif; color: var(--ink); }
  .canvas { position: relative; width: 1200px; height: 1090px; overflow: hidden; background: var(--stone); }

  .top-band { position: absolute; left: 0; top: 0; width: 1200px; height: 82px; background: var(--blue); }
  .brand { position: absolute; left: 537px; top: -41px; width: 128px; height: 128px; border-radius: 50%;
    background: var(--white); display: flex; align-items: flex-end; justify-content: center; padding-bottom: 30px; }
  .brand-name { font-family: "Fredoka", sans-serif; font-weight: 600; font-size: 26px; color: var(--blue); }

  .page-bar { position: absolute; left: 121px; top: 82px; width: 957px; height: 46px; background: var(--panel);
    display: flex; align-items: center; padding-left: 26px; }
  .page-bar-dot { width: 19px; height: 19px; border-radius: 50%; background: var(--green); margin-right: 28px; }
  .page-bar-title { font-family: "Fredoka", sans-serif; font-weight: 500; font-size: 22px; color: var(--blue); letter-spacing: 0.5px; }

  .steps { position: absolute; left: 0; top: 128px; width: 1200px; height: 222px; }
  .step-label { position: absolute; top: 280px; font-family: "Fredoka", sans-serif; font-weight: 500; font-size: 28px;
    color: var(--blue); transform: translateX(-50%); letter-spacing: 0.5px; }
  .step-label.is-current { color: var(--green); top: 282px; }

  .section-band { position: absolute; left: 121px; top: 350px; width: 957px; height: 47px; background: var(--green);
    color: var(--white); font-family: "Fredoka", sans-serif; font-weight: 600; font-size: 35px; text-align: center; line-height: 47px; }
  .content { position: absolute; left: 121px; top: 397px; width: 957px; height: 576px; background: var(--panel); }

  .card { position: absolute; background: var(--white); }
  .member-card { left: 195px; top: 431px; width: 295px; height: 93px; }
  .membership-card { left: 195px; top: 533px; width: 295px; height: 96px; }
  .field { position: absolute; font-size: 10px; font-weight: 900; white-space: nowrap; }
  .field-label { left: 24px; color: var(--ink); }
  .field-value { color: var(--green); }
  .member-card .field-value { left: 159px; }
  .membership-card .field-value { left: 157px; }
  .select-icon { position: absolute; left: 231px; width: 10px; height: 10px; }

  .fee-card { left: 514px; top: 431px; width: 490px; height: 198px; }
  .fee-label { position: absolute; left: 19px; font-size: 20px; color: var(--ink); line-height: 1.2; }
  .fee-value { position: absolute; left: 194px; font-size: 20px; color: var(--green); }
  .fee-icon { position: absolute; left: 424px; width: 46px; height: 46px; }

  .notes-card { left: 196px; top: 657px; width: 808px; height: 175px; }
  .notes-title { position: absolute; left: 22px; top: 15px; font-weight: 900; font-size: 21px; letter-spacing: 1px; }

  .pay-button { position: absolute; left: 514px; top: 865px; width: 171px; height: 44px; background: var(--blue); border: 0;
    color: var(--white); font-family: "Lato", sans-serif; font-weight: 900; font-size: 33px; letter-spacing: 3px; line-height: 44px; text-align: center; }

  .bottom-band { position: absolute; left: 0; top: 973px; width: 1200px; height: 117px; background: var(--blue); }
</style>
</head>
<body>
<div class="canvas">
  <header class="top-band">
    <div class="brand"><span class="brand-name">zumoKet</span></div>
  </header>

  <div class="page-bar"><span class="page-bar-dot"></span><span class="page-bar-title">Make a Payment</span></div>

  <svg class="steps" viewBox="0 0 1200 222" aria-label="Payment steps">
    <g fill="var(--blue)">
      <circle cx="256" cy="91" r="61"/><path d="M282 140 L310 155 L300 124 Z"/>
      <circle cx="452" cy="91" r="61"/><path d="M478 140 L506 155 L496 124 Z"/>
      <circle cx="942" cy="91" r="61"/><path d="M968 140 L996 155 L986 124 Z"/>
    </g>
    <g fill="var(--green)">
      <circle cx="746" cy="91" r="61"/><path d="M772 140 L800 155 L790 124 Z"/>
    </g>
    <text x="256" y="91" text-anchor="middle" font-family="Lato, sans-serif" font-weight="900" font-size="38" fill="#fff">GET</text>
    <text x="256" y="118" text-anchor="middle" font-family="Lato, sans-serif" font-weight="900" font-size="17" fill="#fff">STRATED</text>
    <g fill="#fff">
      <path d="M425 74 L455 56 L466 70 L436 88 Z"/>
      <rect x="421" y="82" width="63" height="40" rx="3"/>
    </g>
    <rect x="428" y="92" width="11" height="3" fill="var(--blue)"/>
    <circle cx="465" cy="113" r="4" fill="var(--blue)"/><circle cx="472" cy="113" r="4" fill="var(--blue)"/>
    <g fill="none" stroke="#fff" stroke-width="4" stroke-linecap="round">
      <rect x="713" y="55" width="60" height="72" rx="6"/>
      <circle cx="726" cy="71" r="4"/><line x1="738" y1="71" x2="760" y2="71"/>
      <circle cx="726" cy="90" r="4"/><line x1="738" y1="90" x2="756" y2="90"/>
      <circle cx="726" cy="109" r="4"/><line x1="738" y1="109" x2="748" y2="109"/>
      <rect x="909" y="55" width="60" height="72" rx="6"/>
      <circle cx="922" cy="71" r="4"/><line x1="934" y1="71" x2="956" y2="71"/>
      <circle cx="922" cy="90" r="4"/><line x1="934" y1="90" x2="956" y2="90"/>
      <circle cx="922" cy="109" r="4"/><line x1="934" y1="109" x2="944" y2="109"/>
    </g>
    <path d="M762 113 L782 93 L790 101 L770 121 L760 123 Z" fill="#fff" stroke="var(--green)" stroke-width="2"/>
    <circle cx="968" cy="115" r="15" fill="var(--blue)" stroke="#fff" stroke-width="3"/>
    <path d="M960 115 L966 121 L976 109" fill="none" stroke="#fff" stroke-width="3" stroke-linecap="round"/>
    <g fill="#fff">
      <rect x="322" y="90" width="42" height="9"/><path d="M360 78 L386 94 L360 111 Z"/>
      <rect x="570" y="90" width="58" height="9"/><path d="M574 78 L550 94 L574 111 Z"/><path d="M624 78 L648 94 L624 111 Z"/>
      <rect x="813" y="90" width="42" height="9"/><path d="M851 78 L877 94 L851 111 Z"/>
    </g>
  </svg>
  <span class="step-label" style="left:254px">Start</span>
  <span class="step-label" style="left:451px">Payment</span>
  <span class="step-label is-current" style="left:743px">Review</span>
  <span class="step-label" style="left:941px">Confirm</span>

  <div class="section-band">Pay Bill</div>
  <main class="content"></main>

  <section class="card member-card">
    <span class="field field-label" style="top:20px">First Name:</span><span class="field field-value" style="top:20px">Join</span>
    <span class="field field-label" style="top:41px">Surname:</span><span class="field field-value" style="top:41px">Rai</span>
    <span class="field field-label" style="top:62px">Fiscal code:</span><span class="field field-value" style="top:62px">012345689</span>
  </section>

  <section class="card membership-card">
    <span class="field field-label" style="top:19px">Association Name:</span><span class="field field-value" style="top:19px">Association</span>
    <span class="field field-label" style="top:43px">Entry category:</span><span class="field field-value" style="top:43px">Category</span>
    <span class="field field-label" style="top:69px">Reference year:</span><span class="field field-value" style="top:69px">Reference</span>
    <svg class="select-icon" style="top:20px" viewBox="0 0 10 10"><circle cx="5" cy="5" r="4.3" fill="none" stroke="#111" stroke-width="1"/><path d="M3 4 L5 6.3 L7 4" fill="none" stroke="#111" stroke-width="1.2"/></svg>
    <svg class="select-icon" style="top:44px" viewBox="0 0 10 10"><circle cx="5" cy="5" r="4.3" fill="none" stroke="#111" stroke-width="1"/><path d="M3 4 L5 6.3 L7 4" fill="none" stroke="#111" stroke-width="1.2"/></svg>
    <svg class="select-icon" style="top:70px" viewBox="0 0 10 10"><circle cx="5" cy="5" r="4.3" fill="none" stroke="#111" stroke-width="1"/><path d="M3 4 L5 6.3 L7 4" fill="none" stroke="#111" stroke-width="1.2"/></svg>
  </section>

  <section class="card fee-card">
    <span class="fee-label" style="top:22px">Fee to be paid:</span><span class="fee-value" style="top:25px">$154.27</span>
    <span class="fee-label" style="top:79px">Expiration date:</span><span class="fee-value" style="top:82px">10.08.2018</span>
    <span class="fee-label" style="top:128px">Extension applied<br>&nbsp;after expiration:</span><span class="fee-value" style="top:141px">Extension</span>
    <svg class="fee-icon" style="top:13px" viewBox="0 0 46 46">
      <path d="M5 18 L24 6 L31 15 L12 27 Z" fill="var(--icon)"/>
      <rect x="3" y="22" width="40" height="20" rx="2" fill="var(--icon)"/>
      <rect x="7" y="27" width="7" height="2" fill="#fff"/>
      <circle cx="32" cy="37" r="2.5" fill="#fff"/><circle cx="37" cy="37" r="2.5" fill="#fff"/>
    </svg>
    <svg class="fee-icon" style="top:73px" viewBox="0 0 46 46">
      <circle cx="23" cy="23" r="21" fill="var(--icon)"/>
      <circle cx="23" cy="23" r="14" fill="none" stroke="#fff" stroke-width="2"/>
      <path d="M23 13 L23 23 L30 23" fill="none" stroke="#fff" stroke-width="2"/>
    </svg>
    <svg class="fee-icon" style="top:126px" viewBox="0 0 46 46">
      <circle cx="23" cy="23" r="20" fill="none" stroke="var(--icon)" stroke-width="2.5"/>
      <path d="M17 21 V16 A6 6 0 0 1 29 16 V21" fill="none" stroke="var(--icon)" stroke-width="2.5"/>
      <rect x="14" y="21" width="18" height="14" fill="none" stroke="var(--icon)" stroke-width="2.5"/>
      <line x1="23" y1="21" x2="23" y2="35" stroke="var(--icon)" stroke-width="2"/>
      <line x1="14" y1="28" x2="32" y2="28" stroke="var(--icon)" stroke-width="2"/>
    </svg>
  </section>

  <section class="card notes-card"><h2 class="notes-title">Notes:</h2></section>

  <button class="pay-button" type="button">PAY</button>

  <footer class="bottom-band"></footer>
</div>
</body>
</html>
```